Briefpapier, Visitenkarten, Bindemappe, Brieumschläge....
Zielgruppe
Steuerberatung vorwiegen für Unternehmer
Aufgabenstellung
Ein Logo ist bereits vorhanden (siehe Analgen) kann aber gerne auch bei einer guten Idee modernisiert werden. Ganz ein neues Logo möchte ich meinen Kunden jedoch ersparen, da ich es erst von zwei Jahren gewechselt habe. Grundfarbe grün wie Pantone 2293 C.
Als Anhaltspunkt was derzeit bei im Einsatz ist, habe ich die entsprechenden Dateien hochgeladen.

```html
<!DOCTYPE html>
<html lang="de">
<head>
<meta charset="utf-8">
<title>Geschäftsausstattung Steuerberater Jonas Berger</title>
<link href="https://fonts.googleapis.com/css2?family=Barlow+Semi+Condensed:wght@400;500;600&display=swap" rel="stylesheet">
<style>
  :root{
    --green:#86c400;
    --ink:#4a4a4a;
    --dark:#1e1e1e;
    --blush:#f9ece8;
    --paper:#ffffff;
    --bg:#ffffff;
  }
  *{box-sizing:border-box;margin:0;padding:0}
  html,body{width:973px;height:1200px;overflow:hidden;background:var(--bg)}
  body{position:relative;font-family:"Barlow Semi Condensed",sans-serif;color:var(--ink)}
  .sheet{position:absolute;background:var(--paper);box-shadow:0 0 3px rgba(0,0,0,.25)}

  /* wordmark */
  .wordmark{position:absolute;display:flex;align-items:center;gap:6px;color:var(--dark);font-weight:600;text-transform:uppercase;line-height:1;letter-spacing:.08em}
  .wordmark .lines{display:flex;flex-direction:column;align-items:flex-end}
  .wordmark .sq{background:var(--green);flex:none}

  /* letterhead */
  .letterhead{left:41px;top:132px;width:588px;height:831px}
  .band{position:absolute;left:0;right:0;height:11px;background:var(--green)}
  .band.top{top:0}.band.bottom{bottom:0}
  .letterhead .wordmark{left:66px;top:79px;font-size:13px}
  .letterhead .wordmark .sq{width:30px;height:30px}
  .contact{position:absolute;font-size:7.6px;line-height:9.5px}
  .contact .name,.contact .role{color:var(--green)}
  .contact .name{font-weight:600;font-size:8.4px}
  .contact p+p{margin-top:9.5px}
  .letterhead .contact{left:475px;top:37px;height:107px;border-left:1px solid var(--green);padding-left:6px;padding-top:2px}
  .sender{position:absolute;left:69px;top:156px;font-size:6.2px;color:var(--dark)}
  .sender b{color:var(--green);font-weight:600}

  /* notepad */
  .notepad{left:674px;top:317px;width:249px;height:249px;border:1px solid #555}
  .notepad .tint{position:absolute;left:0;right:0;top:0;height:66px;background:var(--blush)}
  .notepad .wordmark{left:11px;top:207px;font-size:9px;gap:5px}
  .notepad .wordmark .sq{width:21px;height:21px}
  .notepad .hotline{position:absolute;right:12px;top:209px;text-align:right;color:var(--green);font-weight:600;font-size:8px;line-height:10px}

  /* sticky strips */
  .strip{position:absolute;top:599px;height:154px;background:var(--paper);box-shadow:0 0 3px rgba(0,0,0,.25);overflow:hidden}
  .strip.plain{left:718px;width:70px;border-left:9px solid var(--green);border-right:7px solid var(--green)}
  .strip.folded{left:807px;width:72px;border-left:9px solid var(--green);border-radius:7px;clip-path:polygon(0 0,100% 0,100% 62%,10% 100%,0 100%)}
  .strip.folded::after{content:"";position:absolute;right:0;top:0;width:7px;height:96px;background:var(--green)}
  .strip .wordmark{left:26px;top:6px;flex-direction:column-reverse;font-size:7px;gap:4px}
  .strip .wordmark .lines{writing-mode:vertical-rl;transform:rotate(180deg);align-items:flex-start}
  .strip .wordmark .sq{width:17px;height:17px}

  /* business cards */
  .card{top:996px;width:238px;height:153px}
  .card.front{left:86px;background:var(--green)}
  .card.front .wordmark{left:22px;top:60px;font-size:13px;color:var(--paper)}
  .card.front .wordmark .sq{width:30px;height:30px;background:var(--paper)}
  .card.back{left:346px;border:1px solid #555}
  .card.back .sq{position:absolute;left:45px;top:61px;width:32px;height:32px;background:var(--green)}
  .card.back .contact{left:121px;top:24px}
</style>
</head>
<body>

<section class="sheet letterhead" aria-label="Briefbogen">
  <div class="band top"></div>
  <div class="wordmark"><div class="lines"><span>Steuerberater</span><span>Jonas Berger</span></div><span class="sq"></span></div>
  <div class="contact">
    <p><span class="name">Jonas Berger</span><br><span class="role">Steuerberater</span></p>
    <p>Lindenweg 4<br>86150 Musterau</p>
    <p>Tel.: 0821 / 555 12 – 30<br>Fax: 0821 / 555 12 – 31</p>
    <p>info@kanzlei-berger.de<br>www.kanzlei-berger.de</p>
  </div>
  <p class="sender"><b>Jonas Berger</b> Steuerberater • Lindenweg 4 • 86150 Musterau</p>
  <div class="band bottom"></div>
</section>

<section class="sheet notepad" aria-label="Notizblock">
  <div class="tint"></div>
  <div class="wordmark"><div class="lines"><span>Steuerberater</span><span>Jonas Berger</span></div><span class="sq"></span></div>
  <p class="hotline">0821 / 555 12 – 30<br>www.kanzlei-berger.de</p>
  <div class="band bottom"></div>
</section>

<section class="strip plain" aria-label="Haftnotiz">
  <div class="wordmark"><div class="lines"><span>Steuerberater</span><span>Jonas Berger</span></div><span class="sq"></span></div>
</section>
<section class="strip folded" aria-label="Haftnotiz mit Eselsohr">
  <div class="wordmark"><div class="lines"><span>Steuerberater</span><span>Jonas Berger</span></div><span class="sq"></span></div>
</section>

<section class="sheet card front" aria-label="Visitenkarte Vorderseite">
  <div class="wordmark"><div class="lines"><span>Steuerberater</span><span>Jonas Berger</span></div><span class="sq"></span></div>
</section>

<section class="sheet card back" aria-label="Visitenkarte Rückseite">
  <span class="sq"></span>
  <div class="contact">
    <p><span class="name">Jonas Berger</span><br><span class="role">Steuerberater</span></p>
    <p>Lindenweg 4<br>86150 Musterau</p>
    <p>Tel.: 0821 / 555 12 – 30<br>Fax: 0821 / 555 12 – 31</p>
    <p>info@kanzlei-berger.de<br>www.kanzlei-berger.de</p>
  </div>
</section>

</body>
</html>
```